Pebble and Pine App design

I need a full app design, colours, images, fonts, and a mock up design of the app to bring to the developer.

Pebble and Pine is a free app that allows cafes, independent cafe and chains of cafes to let their customers know what the soup of the day and what specials they have on that day through the app. Each cafe will have a profile which they can upload the Pebble and Pine daily.

The user home screen will include google maps showing their location with the registered cafes and eateries around them. including a list of the cafe and distances below. as seen in attachment.

Target Market(s)

Cafes , anyone who enjoys eating soups and off local cafe specials boards

Requirements
Must have
• I would like a complete app design based on the attached images.

```html
<!DOCTYPE html>
<html lang="en">
<head>
<meta charset="utf-8">
<title>Pebble and Pine – App Screens</title>
<link href="https://fonts.googleapis.com/css2?family=Inter:wght@400;500;600;700;800&display=swap" rel="stylesheet">
<style>
:root{
  --orange:#f76707;
  --orange-soft:#fde3d6;
  --heart:#f0364a;
  --ink:#111111;
  --text:#4a4a4a;
  --muted:#8a8a8a;
  --line:#e4e4e4;
  --surface:#ffffff;
  --panel:#f3f3f3;
  --row:#f2f2f2;
  --map:#ececec;
  --blue:#1a73e8;
}
*{box-sizing:border-box;margin:0;padding:0}
html,body{width:1200px;height:891px;overflow:hidden;background:#fff;font-family:"Inter",sans-serif;color:var(--ink)}
.canvas{position:relative;width:1200px;height:891px}
.screen{position:absolute;top:160px;width:264px;height:574px;border-radius:26px;overflow:hidden;background:var(--surface);border:1px solid var(--line)}
.screen--map{left:145px}
.screen--soups{left:470px}
.screen--cafe{left:790px}
svg.icon{fill:none;stroke:currentColor;stroke-width:1.6;stroke-linecap:round;stroke-linejoin:round}

/* bottom navigation */
.tabbar{position:absolute;left:0;right:0;bottom:0;height:58px;background:#fff;box-shadow:0 -2px 8px rgba(0,0,0,.05)}
.tab{position:absolute;top:14px;width:40px;margin-left:-20px;text-align:center;color:#8e8e8e;font-size:5.5px}
.tab svg{width:20px;height:20px;display:block;margin:0 auto 4px}
.tab--active{color:var(--orange)}
.tab--active::after{content:"";display:block;width:3px;height:3px;border-radius:50%;background:var(--orange);margin:3px auto 0}
.fab{position:absolute;left:111px;top:-9px;width:42px;height:42px;border-radius:50%;background:var(--orange);box-shadow:0 4px 10px rgba(247,103,7,.35);display:flex;align-items:center;justify-content:center}
.fab svg{width:18px;height:18px;fill:#fff;stroke:none}

/* map screen */
.map{position:absolute;inset:0;background:linear-gradient(160deg,#f1f1f1,#e6e6e6 60%,#efefef)}
.search{position:absolute;left:15px;top:36px;width:232px;height:31px;background:#fff;border-radius:16px;box-shadow:0 3px 10px rgba(0,0,0,.1);display:flex;align-items:center;padding:0 10px;gap:8px;color:#a9a9a9;font-size:10px}
.search svg{width:13px;height:13px;color:var(--orange)}
.search .arrow{margin-left:auto;color:#b5b5b5}
.marker{position:absolute;width:12px;height:12px;border-radius:50%;background:var(--orange);border:2px solid #fff;box-shadow:0 1px 3px rgba(0,0,0,.2)}
.me{position:absolute;left:54px;top:213px;width:14px;height:14px;border-radius:50%;background:var(--blue);border:2px solid #fff;box-shadow:0 0 0 5px rgba(26,115,232,.15)}
.big-pin{position:absolute;left:133px;top:217px;width:26px;height:32px;color:var(--orange)}
.locate{position:absolute;left:226px;top:253px;width:27px;height:27px;border-radius:50%;background:#fff;box-shadow:0 2px 6px rgba(0,0,0,.15);display:flex;align-items:center;justify-content:center;color:#777}
.locate svg{width:12px;height:12px}
.cafe-card{position:absolute;left:4px;top:401px;width:240px;height:102px;background:#fff;border-radius:12px;box-shadow:0 3px 12px rgba(0,0,0,.12);padding:11px;display:flex;gap:10px}
.cafe-card--peek{left:253px;width:40px;padding:0}
.cafe-card__photo{width:78px;height:78px;border-radius:9px;background:linear-gradient(135deg,#3d352c,#d9a441 55%,#f0c96a)}
.cafe-card__body{flex:1;position:relative}
.cafe-card__name{font-size:12.5px;font-weight:700;line-height:1}
.cafe-card__dist{position:absolute;right:0;top:1px;color:var(--orange);font-size:8px;font-weight:600}
.rating{display:flex;align-items:center;gap:3px;margin-top:2px}
.stars{color:var(--orange);font-size:6px;letter-spacing:.3px}
.rating small{color:var(--muted);font-size:5px}
.cafe-card__menu{margin-top:6px;background:var(--row);border-radius:3px;padding:4px 4px 4px 16px;display:grid;grid-template-columns:1fr 1fr;font-size:5.5px;color:#444;line-height:1.5;position:relative}
.cafe-card__menu svg{position:absolute;left:3px;top:4px;width:9px;height:9px;color:var(--orange)}
.cafe-card__special{margin-top:4px;background:var(--row);border-radius:3px;padding:3px 4px 3px 18px;font-size:5.3px;color:var(--orange);font-weight:600;position:relative}
.cafe-card__special svg{position:absolute;left:3px;top:2px;width:9px;height:9px}

/* soups screen */
.soups-header{position:absolute;inset:0 0 auto 0;height:300px;background:var(--panel);clip-path:polygon(0 0,100% 0,100% 62%,70% 40%,0 46%)}
.soups-header__shape{position:absolute;left:60px;top:-60px;width:260px;height:220px;border-radius:50%;background:#e6e6e6}
.soup-photo{position:absolute;left:184px;top:-10px;width:150px;height:150px;border-radius:50%;border:6px solid #fff;background:radial-gradient(circle at 45% 45%,#e58a3c,#b8402a 55%,#6b2a1c)}
.soups-title{position:absolute;left:18px;top:58px;font-size:26px;font-weight:800;color:var(--orange);letter-spacing:.3px}
.soups-intro{position:absolute;left:18px;top:94px;width:160px;font-size:11px;line-height:1.35;color:#777}
.soup-list{position:absolute;left:13px;top:150px;width:241px}
.soup-item{height:44px;margin-bottom:10.5px;background:#fff;border-radius:6px;box-shadow:0 1px 5px rgba(0,0,0,.06);display:flex;align-items:center;padding:0 10px 0 5px}
.soup-item__icon{width:34px;height:34px;border-radius:5px;background:var(--orange-soft);display:flex;align-items:center;justify-content:center;color:var(--orange)}
.soup-item__icon svg{width:19px;height:19px}
.soup-item__name{margin-left:18px;font-size:11.5px;font-weight:500;color:#333;flex:1}
.heart{width:15px;height:14px;fill:#dedede;stroke:none}
.heart--on{fill:var(--heart)}

/* cafe screen */
.cafe-photo{position:absolute;left:0;top:0;width:100%;height:125px;background:linear-gradient(170deg,#3b4a3a,#6e5a3d 40%,#c97a3a 75%,#8a5a3a)}
.cafe-sheet{position:absolute;left:0;right:0;top:113px;bottom:0;background:#fff;border-radius:14px 14px 0 0;padding:13px 18px}
.cafe-sheet h1{font-size:17px;font-weight:700;letter-spacing:-.2px}
.cafe-rating{display:flex;align-items:center;gap:6px;margin-top:6px}
.cafe-rating .stars{font-size:12px;letter-spacing:1px}
.cafe-rating small{color:var(--muted);font-size:7.5px}
.address{display:flex;align-items:center;gap:5px;margin-top:10px;font-size:8px;color:#444}
.address svg{width:8px;height:8px;fill:#444;stroke:none}
.about{margin-top:9px;font-size:7.6px;line-height:1.38;color:#666}
.cta{display:block;margin-top:9px;height:26px;border-radius:4px;background:var(--orange);color:#fff;font-size:10px;font-weight:500;text-align:center;line-height:26px}
.menu{margin-top:19px}
.menu__head{height:13px;background:var(--orange-soft);border-radius:2px;display:flex;align-items:center;gap:5px;padding-left:5px;color:var(--orange);font-size:9px;font-weight:700;margin-bottom:7px}
.menu__head svg{width:10px;height:10px}
.menu__row{height:22px;background:var(--row);border-radius:2px;display:flex;align-items:center;justify-content:space-between;padding:0 7px;margin-bottom:6px;font-size:10.5px;color:#444}
.menu__row span:last-child{color:var(--orange)}
.menu__head--special{margin-top:4px}
</style>
</head>
<body>
<svg width="0" height="0" style="position:absolute" aria-hidden="true">
  <defs>
    <symbol id="i-bowl" viewBox="0 0 24 24"><path d="M3 11h18a9 7 0 0 1-18 0z"/><path d="M8 20h8"/><path d="M10.5 4c-.6 1 .6 1.8 0 3M13.5 4c-.6 1 .6 1.8 0 3"/></symbol>
    <symbol id="i-cloche" viewBox="0 0 24 24"><path d="M2 18h20"/><path d="M4 18a8 8 0 0 1 16 0"/><path d="M12 10V8"/></symbol>
    <symbol id="i-heart" viewBox="0 0 24 22"><path d="M12 21S2 14.5 2 7.5A5 5 0 0 1 12 5a5 5 0 0 1 10 2.5C22 14.5 12 21 12 21z"/></symbol>
    <symbol id="i-gear" viewBox="0 0 24 24"><circle cx="12" cy="12" r="3.2"/><circle cx="12" cy="12" r="8" stroke-dasharray="3 2.3"/><circle cx="12" cy="12" r="6.2"/></symbol>
    <symbol id="i-pin" viewBox="0 0 24 24"><path d="M12 23s-8-7.5-8-13.5a8 8 0 0 1 16 0C20 15.5 12 23 12 23z"/></symbol>
    <symbol id="i-search" viewBox="0 0 24 24"><circle cx="11" cy="11" r="8"/><path d="M17 17l4 4"/></symbol>
  </defs>
</svg>

<main class="canvas">

  <!-- Map home -->
  <section class="screen screen--map">
    <div class="map" role="img" aria-label="Street map of the surrounding neighbourhood"></div>
    <div class="search">
      <svg class="icon"><use href="#i-search"/></svg>
      <span>Search here</span>
      <svg class="icon arrow" width="14" height="14" viewBox="0 0 24 24"><path d="M4 12h16M14 6l6 6-6 6"/></svg>
    </div>
    <span class="marker" style="left:143px;top:100px"></span>
    <span class="marker" style="left:139px;top:132px"></span>
    <span class="marker" style="left:52px;top:152px"></span>
    <span class="marker" style="left:227px;top:150px"></span>
    <span class="marker" style="left:39px;top:295px"></span>
    <span class="me"></span>
    <svg class="big-pin" viewBox="0 0 24 30"><path d="M12 29S1 19 1 12a11 11 0 0 1 22 0c0 7-11 17-11 17z" fill="currentColor"/><circle cx="12" cy="12" r="7" fill="#fff"/><path d="M8 12h8a4 3 0 0 1-8 0z" fill="currentColor"/></svg>
    <div class="locate"><svg class="icon" viewBox="0 0 24 24"><circle cx="12" cy="12" r="6"/><circle cx="12" cy="12" r="2" fill="currentColor"/><path d="M12 2v3M12 19v3M2 12h3M19 12h3"/></svg></div>

    <article class="cafe-card">
      <div class="cafe-card__photo" role="img" aria-label="Bowls of noodle soup"></div>
      <div class="cafe-card__body">
        <h2 class="cafe-card__name">Cafe Lumen</h2>
        <span class="cafe-card__dist">➤ 250m</span>
        <div class="rating"><span class="stars">★★★★☆</span><small>23 reviews</small></div>
        <div class="cafe-card__menu">
          <svg class="icon"><use href="#i-bowl"/></svg>
          <span>• Carrot+Corriander</span><span>• Chicken Soup</span>
          <span>• Chicken Ramen</span><span>• Vege Soup</span>
          <span>• Gazpacho</span>
        </div>
        <div class="cafe-card__special"><svg class="icon"><use href="#i-cloche"/></svg>Cauliflower Basil Soup</div>
      </div>
    </article>
    <div class="cafe-card cafe-card--peek"></div>

    <nav class="tabbar">
      <div class="tab" style="left:31px"><svg class="icon"><use href="#i-bowl"/></svg>Soup</div>
      <div class="tab" style="left:81px"><svg class="icon"><use href="#i-cloche"/></svg>Special</div>
      <div class="fab"><svg><use href="#i-pin"/></svg></div>
      <div class="tab" style="left:182px"><svg class="icon"><use href="#i-heart"/></svg>Favorites</div>
      <div class="tab" style="left:232px"><svg class="icon"><use href="#i-gear"/></svg>Settings</div>
    </nav>
  </section>

  <!-- Soups list -->
  <section class="screen screen--soups">
    <div class="soups-header"><div class="soups-header__shape"></div></div>
    <div class="soup-photo" role="img" aria-label="Bowl of ramen soup"></div>
    <h1 class="soups-title">SOUPS</h1>
    <p class="soups-intro">Lorem ipsum dolor sit amet, consectetuer adipiscing elit, sed diam</p>
    <ul class="soup-list" style="list-style:none">
      <li class="soup-item"><span class="soup-item__icon"><svg class="icon"><use href="#i-bowl"/></svg></span><span class="soup-item__name">Carrot+Corriander</span><svg class="heart heart--on"><use href="#i-heart"/></svg></li>
      <li class="soup-item"><span class="soup-item__icon"><svg class="icon"><use href="#i-bowl"/></svg></span><span class="soup-item__name">Pumpkin soup</span><svg class="heart"><use href="#i-heart"/></svg></li>
      <li class="soup-item"><span class="soup-item__icon"><svg class="icon"><use href="#i-bowl"/></svg></span><span class="soup-item__name">Gazpacho</span><svg class="heart"><use href="#i-heart"/></svg></li>
      <li class="soup-item"><span class="soup-item__icon"><svg class="icon"><use href="#i-bowl"/></svg></span><span class="soup-item__name">Chicken Ramen</span><svg class="heart"><use href="#i-heart"/></svg></li>
      <li class="soup-item"><span class="soup-item__icon"><svg class="icon"><use href="#i-bowl"/></svg></span><span class="soup-item__name">Soba</span><svg class="heart heart--on"><use href="#i-heart"/></svg></li>
      <li class="soup-item"><span class="soup-item__icon"><svg class="icon"><use href="#i-bowl"/></svg></span><span class="soup-item__name">Vege soup</span><svg class="heart heart--on"><use href="#i-heart"/></svg></li>
      <li class="soup-item"><span class="soup-item__icon"><svg class="icon"><use href="#i-bowl"/></svg></span><span class="soup-item__name">Beef soup</span><svg class="heart"><use href="#i-heart"/></svg></li>
    </ul>
    <nav class="tabbar">
      <div class="tab tab--active" style="left:31px"><svg class="icon"><use href="#i-bowl"/></svg>Soup</div>
      <div class="tab" style="left:81px"><svg class="icon"><use href="#i-cloche"/></svg>Special</div>
      <div class="fab"><svg><use href="#i-pin"/></svg></div>
      <div class="tab" style="left:182px"><svg class="icon"><use href="#i-heart"/></svg>Favorites</div>
      <div class="tab" style="left:232px"><svg class="icon"><use href="#i-gear"/></svg>Settings</div>
    </nav>
  </section>

  <!-- Cafe profile -->
  <section class="screen screen--cafe">
    <div class="cafe-photo" role="img" aria-label="Close-up of a beef and vegetable stew with rosemary"></div>
    <div class="cafe-sheet">
      <h1>Cafe Hollow</h1>
      <div class="cafe-rating"><span class="stars">★★★★☆</span><small>23 reviews</small></div>
      <p class="address"><svg><use href="#i-pin"/></svg>218 Marlow Lane, Brookvale, 20417</p>
      <p class="about">Lorem ipsum dolor sit amet, consectetuer adipiscing elit, sed diam nonummy nibh euismod tincidunt ut laoreet dolore magna aliquam erat volutpat. Ut wisi enim ad minim veniam, quis nostrud exerci tation ullamcorper suscipit lobortis nisl ut</p>
      <span class="cta">Check full menu</span>
      <div class="menu">
        <div class="menu__head"><svg class="icon"><use href="#i-bowl"/></svg>SOUPS</div>
        <div class="menu__row"><span>Pumpkin soup</span><span>$4.50</span></div>
        <div class="menu__row"><span>Carrot+Corriander</span><span>$7.50</span></div>
        <div class="menu__row"><span>Chicken Ramen</span><span>$8.50</span></div>
        <div class="menu__row"><span>Gazpacho</span><span>$5.50</span></div>
        <div class="menu__row"><span>Carrot+Corriander</span><span>$6.50</span></div>
        <div class="menu__head menu__head--special"><svg class="icon"><use href="#i-cloche"/></svg>SPECIAL</div>
        <div class="menu__row"><span>Beef Steak with Salad</span><span>$19.50</span></div>
      </div>
    </div>
    <nav class="tabbar">
      <div class="tab" style="left:31px"><svg class="icon"><use href="#i-bowl"/></svg>Soup</div>
      <div class="tab" style="left:81px"><svg class="icon"><use href="#i-cloche"/></svg>Special</div>
      <div class="fab"><svg><use href="#i-pin"/></svg></div>
      <div class="tab tab--active" style="left:182px"><svg class="icon"><use href="#i-heart"/></svg>Favorites</div>
      <div class="tab" style="left:232px"><svg class="icon"><use href="#i-gear"/></svg>Settings</div>
    </nav>
  </section>

</main>
</body>
</html>
```